Lumora Drink Mix Packaging Design

We need a packaging design for our new product called "Lumora Drink Mix." This drink mix can help prevent hangovers or lessen their severity if consumed after a night of drinking. Our tagline is: "Feel as good tomorrow morning as you do tonight." Our website is www.lumoradrinkmix.com. We are looking for a design that includes an outer box that contains individual serving packets and the packets themselves. Background color should be black and the colors should be vibrant. Our website uses bright blues, pinks, and purples reminiscent of colors under a blacklight (think club). Our target audience is 30-35 year-old people that occasionally party like they're still 18-21, but then regret it the following day. Please reference our website for additional information on the product.

Target Market(s)

Target market is 30-35 year old men and women that occasionally drink like they're still 18-21.

Industry/Entity Type

Product

Requirements
Must have
• Project must include a box that can hold ~5 individual serving packets inside, as well as the packets inside. Box must contain nutritional information and obligatory FDA disclaimer on one panel, as must the back of the single-serving packets. Package must be black as background with vibrant colors that "pop" and catch someone's eye. Package must include the product name "Lumora Drink Mix." Package must include the company name "Lumora Goods, Inc."
Nice to have
• It should convey fun, friendship, partying, but also safety. Ideally, the tagline: "Feel as good tomorrow morning as you do tonight" should be somewhere on the packaging.
Should not have
• Pictures of people.

```html
<!DOCTYPE html>
<html lang="en">
<head>
<meta charset="utf-8">
<title>Lumora Drink Mix Packaging</title>
<link rel="stylesheet" href="https://fonts.googleapis.com/css2?family=Source+Sans+3:wght@400;700&family=Oswald:wght@400&display=swap">
<style>
  :root {
    --ink: #000000;
    --panel-grey: #e6e6e6;
    --page: #ffffff;
    --white: #ffffff;
    --sky: #35a8de;
    --magenta: #ff1fd2;
    --band: #1a1a1a;
    --glow-blue: #3d8fd0;
    --glow-violet: #7a5ec4;
    --glow-amber: #d98a2a;
    --glow-ember: #8a3a1e;
  }
  * { margin: 0; padding: 0; box-sizing: border-box; }
  html, body {
    width: 1200px; height: 575px; overflow: hidden;
    background: var(--page);
    font-family: "Source Sans 3", "Myriad Pro", sans-serif;
  }
  .canvas { position: relative; width: 1200px; height: 575px; }

  /* flat can labels */
  .label {
    position: absolute; height: 430px;
    background: var(--ink); overflow: hidden; color: var(--white);
  }
  .label > * { z-index: 1; }
  .label--front { left: 36px; top: 84px; width: 240px; }
  .label--back { left: 292px; top: 58px; width: 200px; }
  .label__band {
    position: absolute; left: 0; right: 0; top: 112px; height: 150px;
    background: var(--band); z-index: 0;
  }
  .label__glow {
    position: absolute; left: 0; right: 0; bottom: 0;
    background: linear-gradient(180deg, var(--glow-blue) 0%, var(--glow-violet) 35%, var(--glow-amber) 75%, var(--glow-ember) 100%);
    z-index: 0;
  }
  .label--front .label__glow { height: 170px; }
  .label--back .label__glow { height: 190px; }
  .tagline {
    position: absolute; top: 52px; left: 0; right: 0;
    text-align: center; font-size: 11.5px; letter-spacing: -0.1px;
  }
  .company {
    font-family: "Oswald", sans-serif; color: var(--magenta);
    text-transform: uppercase; text-align: center;
  }
  .label--front .company { position: absolute; top: 98px; left: 0; right: 0; font-size: 11px; }
  .product-name {
    color: var(--sky); font-weight: 700; text-transform: lowercase;
    text-align: center; line-height: 0.92;
  }
  .label--front .product-name { position: absolute; top: 122px; left: 0; right: 0; font-size: 40px; }

  .label--back .product-name { position: absolute; top: 112px; left: 0; right: 0; font-size: 18px; }
  .back-copy {
    position: absolute; top: 182px; left: 14px; right: 14px;
    text-align: center; font-size: 11px; line-height: 1.45;
  }
  .seal {
    position: absolute; top: 318px; left: 42px; width: 40px; height: 16px;
    background: var(--band); border-radius: 2px;
  }
  .nutrition-box {
    position: absolute; top: 342px; left: 42px; width: 90px; height: 46px;
    background: var(--white);
  }

  /* box front panel */
  .box {
    position: absolute; left: 518px; top: 53px; width: 660px; height: 430px;
    background: var(--ink); overflow: hidden;
  }
  .box__sweep { position: absolute; inset: 0; }
  .box__count {
    position: absolute; left: 22px; top: 18px;
    color: var(--sky); font-size: 19px;
  }
  .box__can {
    position: absolute; left: 74px; top: 42px; width: 196px; height: 352px;
    border-radius: 14px 14px 18px 18px;
    background: linear-gradient(180deg, #2a2a2a 0%, #111 12%, #0c0c0c 48%, var(--glow-blue) 62%, var(--glow-violet) 74%, var(--glow-amber) 88%, var(--glow-ember) 100%);
  }
  .box .company { position: absolute; top: 80px; left: 300px; width: 240px; font-size: 17px; }
  .box .product-name { position: absolute; top: 112px; left: 300px; width: 240px; font-size: 72px; }
  .box__web {
    position: absolute; right: 26px; bottom: 14px;
    color: var(--sky); font-size: 16px;
  }
</style>
</head>
<body>
<main class="canvas">

  <section class="label label--front">
    <div class="label__band"></div>
    <div class="label__glow" role="img" aria-label="Blurred multicoloured club lights in blue, violet and amber"></div>
    <p class="tagline">Feel as good tomorrow morning as you do tonight</p>
    <p class="company">Lumora Goods, Inc.</p>
    <h1 class="product-name">Lumora<br>Drink<br>Mix</h1>
  </section>

  <section class="label label--back">
    <div class="label__glow" role="img" aria-label="Blurred multicoloured club lights in blue, violet and amber"></div>
    <p class="product-name">Lumora<br>Drink<br>Mix</p>
    <p class="back-copy">This drink mix can help prevent hangovers or lessen their severity if consumed after a night of drinking.</p>
    <div class="seal" aria-hidden="true"></div>
    <div class="nutrition-box" aria-label="Nutrition facts panel"></div>
  </section>

  <section class="box">
    <svg class="box__sweep" viewBox="0 0 660 430" width="660" height="430" aria-hidden="true">
      <path d="M150,0 H660 V318 C560,380 420,405 330,372 C230,330 130,180 150,0 Z" fill="var(--panel-grey)"/>
    </svg>
    <p class="box__count">5 cans</p>
    <div class="box__can" role="img" aria-label="Can of Lumora Drink Mix with black label and club light pattern"></div>
    <p class="company">Lumora Goods, Inc.</p>
    <h2 class="product-name">Lumora<br>Drink<br>Mix</h2>
    <p class="box__web">www.lumoradrinkmix.com</p>
  </section>

</main>
</body>
</html>
```